Modern Corporate Brochure For Australian Real Estate Agency

We need a corporate 10 page A4 brochure for a Australian Real Estate agency with information for our clients and referral partners.

Main colour scheme: #238b53

Examples of designs:
https://plorvendax.example/item/8-page-corporate-business-brochure/5820417

https://plorvendax.example/item/brochure/7461283

https://plorvendax.example/item/the-company-profile/39851620

https://plorvendax.example/item/brochure-pack-a4trifold-leafletbusiness-card/857312

Target Market(s)

Professional Australians

Industry/Entity Type

Real Estate

Font styles to use
Sans Serif

Requirements
Must have
• Use of multiple greens from the logo

```html
<!DOCTYPE html>
<html lang="en">
<head>
<meta charset="utf-8">
<title>Harlow Ridge Property Group – Brochure Cover Spread</title>
<link rel="stylesheet" href="https://fonts.googleapis.com/css2?family=Anton&family=Montserrat:wght@700;800&family=Open+Sans:ital,wght@0,400;0,700;1,700&display=swap">
<style>
  :root {
    --green: #238b53;
    --green-dark: #1a5e38;
    --green-deep: #154a2d;
    --green-light: #3aa66a;
    --green-band: #2f7a4e;
    --ink: #2d3b33;
    --paper: #ffffff;
    --backdrop: #8c8c8c;
  }
  * { margin: 0; padding: 0; box-sizing: border-box; }
  html, body { width: 908px; height: 1200px; overflow: hidden; }
  body {
    background: var(--backdrop);
    font-family: "Open Sans", Arial, sans-serif;
    color: var(--ink);
    position: relative;
  }
  .spread {
    position: absolute;
    left: 34px; top: 303px;
    width: 840px; height: 594px;
    display: flex;
    box-shadow: 0 10px 30px rgba(0,0,0,.35);
  }
  .page {
    position: relative;
    width: 420px; height: 594px;
    background: var(--paper);
    overflow: hidden;
  }
  .page svg.shapes { position: absolute; inset: 0; width: 420px; height: 594px; }

  .brand {
    position: absolute;
    display: flex; align-items: center; gap: 6px;
    font-family: "Montserrat", Arial, sans-serif;
    font-weight: 700;
    color: var(--green-dark);
    letter-spacing: .3px;
    white-space: nowrap;
  }
  .brand-mark { width: 12px; height: 12px; background: var(--green); flex: none; }

  /* front cover */
  .front .brand { top: 40px; right: 30px; font-size: 12px; }
  .welcome {
    position: absolute; left: 30px; top: 472px;
    transform: rotate(-6deg); transform-origin: left top;
  }
  .welcome-kicker {
    font-family: "Anton", Impact, sans-serif;
    font-size: 26px; line-height: 1; color: var(--green-dark);
    letter-spacing: .5px;
  }
  .welcome-name {
    font-family: "Montserrat", Arial, sans-serif;
    font-weight: 800; font-size: 14.5px; line-height: 1.25;
    color: var(--green-deep); letter-spacing: .5px;
  }
  .welcome-url {
    margin-top: 6px;
    font-size: 9px; font-weight: 700; color: var(--ink);
  }

  /* back cover */
  .about {
    position: absolute; left: 48px; top: 92px; width: 280px;
    transform: rotate(-4deg); transform-origin: left top;
  }
  .about h2, .mission h2 {
    font-family: "Open Sans", Arial, sans-serif;
    font-weight: 700; font-size: 12px; color: var(--green-dark);
    margin-bottom: 6px;
  }
  .about p { font-size: 7.6px; line-height: 1.45; margin-bottom: 8px; color: var(--ink); }
  .mission { margin-top: 14px; }
  .mission p { font-size: 8px; line-height: 1.4; font-style: italic; font-weight: 700; color: var(--ink); width: 210px; }

  .back .brand { left: 190px; top: 478px; font-size: 9.5px; transform: rotate(-6deg); transform-origin: left top; }
  .back-url {
    position: absolute; left: 210px; top: 498px;
    font-size: 8px; font-weight: 700; color: var(--ink);
    transform: rotate(-6deg); transform-origin: left top;
  }
  .contacts {
    position: absolute; left: 22px; top: 486px;
    font-size: 7px; line-height: 1.35;
    transform: rotate(-6deg); transform-origin: left top;
  }
  .contacts h3 { font-size: 7.5px; font-weight: 700; color: var(--green-dark); margin-top: 3px; }
  .contact-line { display: flex; align-items: center; gap: 5px; }
  .contact-icon { width: 8px; height: 8px; flex: none; }
</style>
</head>
<body>
  <main class="spread">
    <!-- Back cover -->
    <section class="page back">
      <svg class="shapes" viewBox="0 0 420 594">
        <defs>
          <linearGradient id="facetBack" x1="0" y1="0" x2="1" y2="1">
            <stop offset="0" stop-color="#2a9a5c"/>
            <stop offset=".5" stop-color="#1f7a47"/>
            <stop offset="1" stop-color="#15522f"/>
          </linearGradient>
        </defs>
        <rect width="420" height="470" fill="url(#facetBack)" role="img" aria-label="Faceted green geometric background"/>
        <polygon points="18,74 398,48 334,444 18,452" fill="none" stroke="#ffffff" stroke-width="3" opacity=".9"/>
        <polygon points="28,80 388,56 326,436 28,444" fill="var(--paper)"/>
        <polygon points="0,472 420,430 420,594 0,594" fill="var(--paper)"/>
        <polygon points="0,576 420,564 420,594 0,594" fill="var(--green-band)"/>
      </svg>

      <div class="about">
        <h2>Harlow Ridge Property Group</h2>
        <p>Harlow Ridge Property Group is one of Queensland's fastest growing property agencies. Our team are driven, focused, trained, and have proven results delivering better service and achieving superior results for their clients than any other agency in the market place. Our team collectively manage over 600 properties and have over 50 years experience between them.</p>
        <p>In total we manage an asset portfolio worth in excess of 200 million and have only been operating since August 2012. Experiencing that kind of growth predominantly via referral means that we must be doing something right. Our clients and associates strongly believe in what we do and appreciate the dedication they receive when allowing Harlow Ridge Property Group the opportunity to manage or sell their largest asset.</p>
        <div class="mission">
          <h2>Our Mission</h2>
          <p>"To provide a superior service that is unmatched in the real estate industry and ensure that all Harlow Ridge Property Group clients achieve the highest possible yields &amp; sale prices for their properties."</p>
        </div>
      </div>

      <div class="brand"><span class="brand-mark"></span>HARLOW RIDGE PROPERTY GROUP</div>
      <div class="back-url">www.harlowridge.example</div>

      <div class="contacts">
        <h3>Brisbane</h3>
        <div class="contact-line">
          <svg class="contact-icon" viewBox="0 0 10 10"><circle cx="5" cy="5" r="5" fill="var(--green)"/><path d="M3 2.6l1 .1.5 1.3-.6.5c.3.7.8 1.2 1.5 1.5l.5-.6 1.3.5.1 1c-2.3.4-4.7-2-4.3-4.3z" fill="#fff"/></svg>
          (07) 3000 4815
        </div>
        <div class="contact-line">
          <svg class="contact-icon" viewBox="0 0 10 10"><circle cx="5" cy="5" r="5" fill="var(--green)"/><rect x="2.4" y="3.2" width="5.2" height="3.6" fill="#fff"/><path d="M2.4 3.2L5 5.3 7.6 3.2" fill="none" stroke="var(--green)" stroke-width=".6"/></svg>
          info@harlowridge.example
        </div>
        <h3>Gladstone</h3>
        <div class="contact-line">
          <svg class="contact-icon" viewBox="0 0 10 10"><circle cx="5" cy="5" r="5" fill="var(--green)"/><path d="M3 2.6l1 .1.5 1.3-.6.5c.3.7.8 1.2 1.5 1.5l.5-.6 1.3.5.1 1c-2.3.4-4.7-2-4.3-4.3z" fill="#fff"/></svg>
          (07) 4000 2716
        </div>
        <div class="contact-line">
          <svg class="contact-icon" viewBox="0 0 10 10"><circle cx="5" cy="5" r="5" fill="var(--green)"/><rect x="2.4" y="3.2" width="5.2" height="3.6" fill="#fff"/><path d="M2.4 3.2L5 5.3 7.6 3.2" fill="none" stroke="var(--green)" stroke-width=".6"/></svg>
          reception.gladstone@harlowridge.example
        </div>
      </div>
    </section>

    <!-- Front cover -->
    <section class="page front">
      <svg class="shapes" viewBox="0 0 420 594">
        <defs>
          <linearGradient id="skyline" x1="0" y1="0" x2="0" y2="1">
            <stop offset="0" stop-color="#3b6fd6"/>
            <stop offset=".45" stop-color="#1d3f8f"/>
            <stop offset=".65" stop-color="#3a2a4a"/>
            <stop offset=".8" stop-color="#6a2f6a"/>
            <stop offset="1" stop-color="#1a2850"/>
          </linearGradient>
          <linearGradient id="facetFront" x1="0" y1="0" x2="1" y2="1">
            <stop offset="0" stop-color="#2a9a5c"/>
            <stop offset="1" stop-color="#15522f"/>
          </linearGradient>
        </defs>
        <polygon points="50,0 420,0 420,210 356,430 0,452 0,196" fill="url(#skyline)" role="img" aria-label="Photograph of a city skyline at dusk reflected in a river"/>
        <polygon points="0,0 42,0 0,172" fill="url(#facetFront)"/>
        <polygon points="420,226 420,594 300,594" fill="url(#facetFront)" role="img" aria-label="Faceted green geometric panel"/>
        <polygon points="0,570 312,552 306,594 0,594" fill="var(--green-band)"/>
      </svg>

      <div class="brand"><span class="brand-mark"></span>HARLOW RIDGE PROPERTY GROUP</div>

      <div class="welcome">
        <div class="welcome-kicker">WELCOME TO</div>
        <div class="welcome-name">HARLOW RIDGE PROPERTY GROUP</div>
        <div class="welcome-url">www.harlowridge.example</div>
      </div>
    </section>
  </main>
</body>
</html>
```